Packaging design for high end, natural skin care line needed

Marisa Holloway Beauty needs a label design. It is a new skin care line I am launching.
For years my line Pure Meadow Beauty was quite popular and featured in several magazines, but for personal reasons had to be shut down. Now I am launching a new line featuring PMB's top selling products, but focused solely on skin care more so than cosmetics. All products will still be handmade, but the line should still look professional-something worthy of a Fresh Larder shelf!
I am branding it with my name, as I am often quoted in articles related to gluten in beauty products, so Marisa Holloway and beauty are key words.
The key products will be facial and body serums which are packaged in .5oz., 1oz. and larger amber glass bottles with black dropper tops, I will include pictures below. For dimensions, the labels can be any size that you think will work best, but need to at the least fit the 1oz. bottle, dimensions shown here http://www.brightvialshop.example/amber-glass-round-vial/p/QX7T-52/
I loved the former PMB logo, but for Marisa Holloway Beauty I am looking for something more personal, more apothecary-like, and probably less colorful.
The line will be small, just a handful of products, but luxe, rich.
I am attaching photos of Pure Meadow Beauty's packaging for your reference.
Thanks much!!
Updates

Hi Everyone! Thank you for your submissions! Please see the links I provided in the brief, I really am looking for something more technical looking, like an apothecary. And want black text on a white background, not a black background, and nothing flowery.
Thank you all!!
Marisa

Target Market(s)

My clients are primarily women of all ages, but with more of a skin care focus, and no longer a cosmetic one, I would also like to appeal to a male audience. My clients are health conscious, gluten-free, natural, paleo, or vegan, etc. Target age is probably 25-55. Products are a bit high end, priced $45-65.

Industry/Entity Type

Cosmetics

Requirements
Must have
• It must at least say Marisa Holloway, or can say Marisa Holloway Beauty, but "Beauty" is not necessary. And capitalization is open, try whatever you think serves the brand. Likely slogans or taglines that can be included but are not essential: Care for your skin. Love and care for your skin. Handmade with love in the USA. Handmade in the USA. Think modern day apothecary. Small batch scotch. Something fine, but custom, handmade.
Nice to have
• I like the aesthetic of Tolmi Skin Care a bit http://www.rosalindtarvey.example.au/
And of Dorian Pelku as shown here http://www.pinboardly.example/pin/584203917660218447/
Also of something like this that is even customizable http://www.pinboardly.example/pin/76920418835102734/
Every product is handmade in small batches, with fine ingredients, a moderate price point of around $45-$65. And I will likely begin making custom orders. So there could be a space to say when it was made, or for whom. I would like to keep the colors classic though, I probably want to stay away from the bright pink on this one.
Should not have
• As I mentioned, probably want to stay away from a lot of color. I like black vs. gray for the text, as it will show up better in editorials. I must look good, but also photograph well. Thanks!

```html
<!DOCTYPE html>
<html lang="en">
<head>
<meta charset="utf-8">
<title>Marisa Holloway – Balancing Facial Serum Label</title>
<link href="https://fonts.googleapis.com/css2?family=Courier+Prime:wght@400;700&display=swap" rel="stylesheet">
<style>
  :root {
    --taupe: #7d746e;
    --ink: #2f2f2f;
    --paper: #ffffff;
    --edge: #e2e2e2;
  }
  html, body {
    margin: 0;
    padding: 0;
    width: 1200px;
    height: 1000px;
    overflow: hidden;
    background: var(--paper);
  }
  body {
    position: relative;
    font-family: "Courier Prime", "Courier New", monospace;
  }
  .label {
    position: absolute;
    left: 55px;
    top: 305px;
    width: 1060px;
    height: 397px;
    background: var(--paper);
    border-left: 1px solid var(--edge);
    border-right: 1px solid var(--edge);
    box-sizing: border-box;
  }
  .band {
    position: absolute;
    left: -1px;
    right: -1px;
    height: 14px;
    background: var(--taupe);
  }
  .band--top { top: 0; }
  .band--bottom { bottom: 0; }

  .panel {
    position: absolute;
    top: 33px;
    font-size: 18.5px;
    line-height: 19.5px;
    margin: 0;
  }
  .panel p { margin: 0; }
  .panel--left { left: 18px; width: 240px; }
  .panel--right { left: 787px; width: 260px; }

  .muted { color: var(--taupe); }
  .dark { color: var(--ink); }

  .claims {
    list-style: none;
    margin: 20px 0 0;
    padding: 0;
    color: var(--ink);
  }
  .claims li::before {
    content: "•";
    color: var(--taupe);
    display: inline-block;
    width: 15px;
    position: relative;
    top: -3px;
    font-size: 15px;
  }
  .handmade { margin-top: 20px !important; }
  .signature {
    position: absolute;
    left: 78px;
    top: 346px;
    width: 94px;
    height: 22px;
    background: linear-gradient(90deg, rgba(47,47,47,0.06), rgba(47,47,47,0.14), rgba(47,47,47,0.06));
    border-radius: 2px;
  }
  .gap { margin-top: 20px !important; }

  .brand {
    position: absolute;
    left: 355px;
    top: 110px;
    display: flex;
    align-items: center;
    gap: 16px;
  }
  .brand__square {
    width: 80px;
    height: 80px;
    background: var(--taupe);
  }
  .brand__name {
    font-size: 40px;
    line-height: 40px;
    color: var(--ink);
  }

  .product-plate {
    position: absolute;
    left: 271px;
    top: 292px;
    width: 463px;
    height: 105px;
    background: var(--taupe);
    color: var(--paper);
    font-size: 27px;
    letter-spacing: 0.5px;
    display: flex;
    align-items: center;
    justify-content: center;
    padding-bottom: 10px;
    box-sizing: border-box;
  }
</style>
</head>
<body>
  <section class="label">
    <div class="band band--top"></div>
    <div class="band band--bottom"></div>

    <div class="panel panel--left">
      <p class="muted">Lorem ipsum dolor sit amet, consectetur adipiscing elit. Pellentesque lorem est.</p>
      <ul class="claims">
        <li>100% Vegan</li>
        <li>Gluten free</li>
        <li>Cruelty free</li>
        <li>No animal testing</li>
        <li>100% Natural</li>
      </ul>
      <p class="dark handmade">Handmade with love in the USA.</p>
    </div>
    <div class="signature" role="img" aria-label="Handwritten signature of M. Holloway"></div>

    <div class="brand">
      <div class="brand__square"></div>
      <div class="brand__name">Marisa<br>Holloway</div>
    </div>

    <div class="product-plate">BALANCING FACIAL SERUM</div>

    <div class="panel panel--right">
      <p class="muted">Ingredients: consect adipiscing elit, Pelle nunc sit, amet, libero nec orci, semper, euismod.</p>
      <p class="dark gap">Directions: Maecenas dapibus posuere velit, sit amet tempus massa placerat ut. Aenean cursus leo id massa.</p>
      <p class="muted gap">www.yourwebsite.example</p>
      <p class="dark gap">Net. wt: 1 oz</p>
    </div>
  </section>
</body>
</html>
```